Window Perf design with eadership quotes

I am wanting to create a window perf that covers windows in a conference room. I have included a picture of the windows. Each window is 26 1/2 inches by 92 inches. I have also included several other pictures to give an example of how I would like the Quotes to look.

Some Quotes I would like to use
1. Your Future is created by what you do today not tomorrow.
2. The answer is Yes
3. People don't care how much you know until they know how much you care.
4. Treat employees like they make a difference and they will.
5. Don't follow the crowd, Let the crowd follow you.
6. Treat people as if they were what they ought to be , and help them become what they are capable of being.
7. Leadership is not a title, its a behavior. LIVE IT
8. We make a living by what we get, We make a life by what we give.
9. Success is not final, failure is not fatal: it is courage to continue that counts.
10. The best way to predict your future is to create it.
11. The supreme quality of leadership is Integrity.
12. Whatever you are, Be a good one

Quotes

• I am imore interested in how this looks rather than including all of the quotes. I also ant this to be a solid background design for privacy.

```html
<!DOCTYPE html>
<html lang="en">
<head>
<meta charset="utf-8">
<title>Leadership Quotes Window Perf</title>
<link rel="stylesheet" href="https://fonts.googleapis.com/css2?family=Abril+Fatface&family=Alfa+Slab+One&family=Bitter:ital,wght@1,700;1,800&family=Great+Vibes&family=Josefin+Slab:wght@700&family=Montserrat:wght@300;400;600;800&family=Oswald:wght@300;400;600&family=Playfair+Display:ital,wght@0,400;0,700;0,900;1,400;1,700&display=swap">
<style>
  :root {
    --page: #e9e7e2;
    --panel: #1b1c1f;
    --frame: #f4f4f2;
    --ink: #f3f3f1;
    --red: #e3262c;
    --grey: #a7adb1;
    --grey-dark: #6f7478;
    --helmet: #d9d9d9;
  }
  * { margin: 0; padding: 0; box-sizing: border-box; }
  html, body { width: 1200px; height: 1000px; overflow: hidden; background: var(--page); }
  .window-perf {
    position: absolute; left: 64px; top: 50px;
    width: 1072px; height: 900px;
    display: flex; gap: 14px; padding: 10px;
    background: var(--frame);
  }
  .pane {
    position: relative; flex: 1; height: 100%;
    background: var(--panel); color: var(--ink);
    text-align: center; line-height: 1;
  }
  .quote { position: absolute; left: 0; right: 0; display: flex; flex-direction: column; align-items: center; }
  .q-top { top: 48px; }
  .q-mid { top: 335px; }
  .q-bottom { top: 605px; }
  .red { color: var(--red); }
  .grey { color: var(--grey); }
  .sans { font-family: "Montserrat", sans-serif; }
  .cond { font-family: "Oswald", sans-serif; }
  .serif { font-family: "Playfair Display", serif; }
  .slab { font-family: "Bitter", serif; font-style: italic; font-weight: 800; }
  .spaced { letter-spacing: .28em; }

  /* Pane 1 */
  .future-your { font: 300 26px "Montserrat", sans-serif; letter-spacing: .35em; margin-bottom: 6px; }
  .future-word { font: 800 34px "Montserrat", sans-serif; letter-spacing: .06em; }
  .future-created { font: 800 26px "Montserrat", sans-serif; margin-top: 4px; }
  .future-created i { font: italic 400 17px "Playfair Display", serif; }
  .future-do { font: 400 29px "Oswald", sans-serif; margin-top: 4px; }
  .future-today { font: 600 30px "Oswald", sans-serif; letter-spacing: .04em; margin-top: 3px; }
  .future-not { display: flex; align-items: center; gap: 4px; margin-top: 3px; }
  .future-not .tag { font: 800 9px "Montserrat", sans-serif; color: var(--red); writing-mode: vertical-rl; transform: rotate(180deg); }
  .future-not .struck { font: 400 26px "Oswald", sans-serif; text-decoration: line-through; text-decoration-color: var(--red); text-decoration-thickness: 3px; }

  .rule { width: 170px; height: 5px; background: var(--ink); }
  .answer-the { font: 700 26px "Josefin Slab", serif; letter-spacing: .4em; margin: 14px 0 4px; }
  .answer-word { font: 700 34px "Josefin Slab", serif; letter-spacing: .12em; }
  .answer-is { display: flex; align-items: center; gap: 8px; font: 400 28px "Playfair Display", serif; letter-spacing: .2em; margin: 4px 0; }
  .answer-is svg { display: block; }
  .answer-yes { font: 72px "Abril Fatface", serif; letter-spacing: .04em; margin-bottom: 14px; }

  .emp-treat { font: 700 23px "Playfair Display", serif; margin-bottom: 12px; }
  .emp-word { font: 400 21px "Montserrat", sans-serif; letter-spacing: .2em; }
  .emp-like { font: italic 400 19px "Playfair Display", serif; margin-top: 6px; }
  .emp-like b { font: italic 800 27px "Bitter", serif; }
  .emp-diff { font: 800 23px "Montserrat", sans-serif; letter-spacing: .05em; margin-top: 6px; }
  .emp-will { font: italic 800 24px "Bitter", serif; margin-top: 4px; }
  .emp-will span { font: 40px "Playfair Display", serif; font-style: italic; }

  /* Pane 2 */
  .care-lead { font: 400 24px "Playfair Display", serif; margin-bottom: 6px; }
  .care-caps { font: 400 26px "Playfair Display", serif; letter-spacing: .14em; margin-top: 6px; }
  .care-italic { font: italic 400 27px "Playfair Display", serif; margin-top: 6px; }

  .crowd-line { font: 400 22px "Montserrat", sans-serif; margin-top: 4px; }
  .crowd-line b { font-weight: 800; font-style: italic; }
  .crowd-red { font: 36px "Alfa Slab One", serif; color: var(--red); letter-spacing: .02em; }
  .crowd-red small { font: 400 15px "Montserrat", sans-serif; color: var(--ink); letter-spacing: .1em; }
  .crowd-follow { font: italic 28px "Alfa Slab One", serif; margin-top: 4px; }
  .crowd-you { position: relative; width: 190px; height: 50px; margin-top: 2px; }
  .crowd-you svg { position: absolute; inset: 0; }
  .crowd-you span { position: absolute; right: 10px; top: 8px; font: italic 36px "Alfa Slab One", serif; }

  .give-caps { font: 400 24px "Montserrat", sans-serif; letter-spacing: .22em; margin-top: 4px; }
  .give-slab { font: italic 800 30px "Bitter", serif; margin-top: 4px; }
  .give-slab .grey { font: 700 32px "Oswald", sans-serif; font-style: normal; }
  .give-big { font: 700 52px "Oswald", sans-serif; color: var(--grey); }

  /* Pane 3 */
  .whatever { font: 600 35px "Oswald", sans-serif; letter-spacing: .12em; }
  .whatever-you { font: 400 24px "Montserrat", sans-serif; letter-spacing: .18em; margin-top: 4px; display: flex; gap: 8px; align-items: center; }
  .be { font: 46px "Alfa Slab One", serif; letter-spacing: .5em; margin: 4px 0 0 .5em; transform: scaleY(.8); }
  .good { font: italic 800 30px "Bitter", serif; margin-left: 60px; }
  .one-row { display: flex; align-items: center; gap: 10px; }
  .helmet { width: 70px; height: 60px; background: var(--helmet); border-radius: 36px 36px 12px 30px; }
  .one { font: 800 44px "Montserrat", sans-serif; color: var(--red); }

  .succ-big { font: 600 30px "Montserrat", sans-serif; letter-spacing: .16em; margin-top: 4px; }
  .succ-small { font: 300 24px "Montserrat", sans-serif; letter-spacing: .1em; margin-top: 3px; }
  .succ-small b { font-weight: 800; letter-spacing: 0; }
  .succ-courage { font: 400 26px "Montserrat", sans-serif; margin-top: 3px; }
  .succ-courage small { font-size: 14px; }
  .succ-continue { font: italic 300 18px "Montserrat", sans-serif; letter-spacing: .1em; margin-top: 3px; }
  .succ-counts { font: 800 30px "Montserrat", sans-serif; letter-spacing: .16em; color: var(--grey); margin-top: 4px; }

  .lead-head { display: flex; align-items: center; gap: 10px; }
  .lead-lines { width: 62px; height: 18px; background: repeating-linear-gradient(var(--ink) 0 2px, transparent 2px 5px); }
  .crown { width: 40px; height: 28px; background: var(--ink); border-radius: 4px 4px 2px 2px; }
  .lead-word { font: 600 30px "Oswald", sans-serif; letter-spacing: .06em; margin-top: 6px; }
  .lead-line { font: italic 400 19px "Playfair Display", serif; margin-top: 4px; }
  .lead-line span { font: 400 23px "Montserrat", sans-serif; letter-spacing: .12em; font-style: italic; }
  .lead-live { font: 400 46px "Oswald", sans-serif; letter-spacing: .1em; margin-top: 2px; }
  .lead-foot { width: 180px; height: 20px; margin-top: 4px; background: repeating-linear-gradient(var(--ink) 0 2px, transparent 2px 6px); }

  /* Pane 4 */
  .sup-the { font: 400 24px "Playfair Display", serif; letter-spacing: .5em; }
  .sup-word { font: 900 34px "Playfair Display", serif; color: var(--grey); letter-spacing: .06em; margin-top: 2px; }
  .sup-quality { font: 46px "Great Vibes", cursive; margin-top: -4px; }
  .sup-caps { font: 400 24px "Playfair Display", serif; letter-spacing: .08em; margin-top: 2px; }
  .sup-integrity { font: 300 44px "Oswald", sans-serif; color: var(--grey-dark); letter-spacing: .14em; transform: scaleY(1.15); margin-top: 10px; }

  .ought { font: italic 700 22px "Playfair Display", serif; line-height: 1.15; }
  .ought .big { font-size: 38px; }
  .ought .amp { font-size: 40px; }

  .predict-caps { font: 400 22px "Montserrat", sans-serif; letter-spacing: .26em; margin-top: 6px; }
  .predict-caps.bold { font-weight: 600; font-size: 24px; }
  .predict-red { font: italic 600 26px "Montserrat", sans-serif; letter-spacing: .18em; color: var(--red); }
  .predict-red small { font: 400 17px "Montserrat", sans-serif; color: var(--ink); font-style: normal; }
  .predict-create { font: 400 30px "Playfair Display", serif; letter-spacing: .14em; color: #7a1e22; margin-top: 6px; }
  .predict-it { font: 400 30px "Oswald", sans-serif; letter-spacing: .1em; margin-top: 4px; }
</style>
</head>
<body>
<main class="window-perf">

  <section class="pane">
    <div class="quote q-top">
      <p class="future-your">YOUR</p>
      <p class="future-word red">FUTURE</p>
      <p class="future-created"><i>is</i>CREATED<i>by</i></p>
      <p class="future-do">WHAT YOU DO</p>
      <p class="future-today"><span class="red">➜</span> TODAY <span class="red">⬅</span></p>
      <p class="future-not"><span class="tag">NOT</span><span class="struck">TOMORROW</span></p>
    </div>
    <div class="quote q-mid">
      <div class="rule"></div>
      <p class="answer-the">•THE•</p>
      <p class="answer-word">answer</p>
      <p class="answer-is">
        <svg width="40" height="14" aria-hidden="true"><g stroke="var(--ink)" stroke-width="2"><line x1="0" y1="2" x2="40" y2="2"/><line x1="0" y1="7" x2="40" y2="7"/><line x1="0" y1="12" x2="40" y2="12"/></g></svg>
        IS
        <svg width="40" height="14" aria-hidden="true"><g stroke="var(--ink)" stroke-width="2"><line x1="0" y1="2" x2="40" y2="2"/><line x1="0" y1="7" x2="40" y2="7"/><line x1="0" y1="12" x2="40" y2="12"/></g></svg>
      </p>
      <p class="answer-yes">YES</p>
      <div class="rule"></div>
    </div>
    <div class="quote q-bottom">
      <p class="emp-treat">Treat</p>
      <p class="emp-word">EMPLOYEES</p>
      <p class="emp-like">like <b>they</b> make a</p>
      <p class="emp-diff">DIFFERENCE</p>
      <p class="emp-will"><span>&amp;</span> they will</p>
    </div>
  </section>

  <section class="pane">
    <div class="quote q-top">
      <p class="care-lead">People don’t care</p>
      <p class="care-caps">HOW MUCH</p>
      <p class="care-caps">YOU KNOW</p>
      <p class="care-italic">until they know</p>
      <p class="care-caps">HOW MUCH</p>
      <p class="care-caps">YOU CARE</p>
    </div>
    <div class="quote q-mid">
      <p class="crowd-line"><b>DON’T</b>FOLLOW</p>
      <p class="crowd-red"><small>THE</small>CROWD</p>
      <p class="crowd-line">LET<small>THE</small>CROWD</p>
      <p class="crowd-follow">FOLLOW</p>
      <div class="crowd-you">
        <svg width="190" height="50" aria-hidden="true"><path d="M160 2 H12 V26 H40" fill="none" stroke="var(--red)" stroke-width="2" stroke-dasharray="6 4"/><path d="M40 20 L50 26 L40 32 Z" fill="var(--red)"/></svg>
        <span>YOU</span>
      </div>
    </div>
    <div class="quote q-bottom">
      <p class="give-caps">WE MAKE</p>
      <p class="give-slab">a living by</p>
      <p class="give-slab">what <span class="grey">WE GET</span></p>
      <p class="give-caps">WE MAKE</p>
      <p class="give-slab">a life by what</p>
      <p class="give-slab">we<span class="give-big">GIVE</span></p>
    </div>
  </section>

  <section class="pane">
    <div class="quote q-top">
      <p class="whatever">WHATEVER</p>
      <p class="whatever-you">YOU<span class="red">★</span>ARE</p>
      <p class="be">BE</p>
      <p class="good">a good</p>
      <div class="one-row">
        <div class="helmet" role="img" aria-label="Football helmet illustration"></div>
        <span class="one">ONE</span>
      </div>
    </div>
    <div class="quote q-mid">
      <p class="succ-big">SUCCESS</p>
      <p class="succ-small">is<b>NOT</b>final</p>
      <p class="succ-big">FAILURE</p>
      <p class="succ-small">is<b>NOT</b>fatal:</p>
      <p class="succ-courage"><small>it is </small>COURAGE</p>
      <p class="succ-continue">to CONTINUE that</p>
      <p class="succ-counts">COUNTS</p>
    </div>
    <div class="quote q-bottom">
      <div class="lead-head">
        <div class="lead-lines"></div>
        <div class="crown" role="img" aria-label="Crown ornament"></div>
        <div class="lead-lines"></div>
      </div>
      <p class="lead-word">LEADERSHIP</p>
      <p class="lead-line">is not a <span>TITLE</span></p>
      <p class="lead-line">it’s a <span>BEHAVIOR</span></p>
      <p class="lead-live">LIVE IT</p>
      <div class="lead-foot"></div>
    </div>
  </section>

  <section class="pane">
    <div class="quote q-top">
      <p class="sup-the">THE</p>
      <p class="sup-word">SUPREME</p>
      <p class="sup-quality">Quality of</p>
      <p class="sup-caps">LEADERSHIP</p>
      <p class="sup-caps">IS</p>
      <p class="sup-integrity">INTEGRITY</p>
    </div>
    <div class="quote q-mid">
      <p class="ought">Treat people as<br>if they were what<br>they ought to <span class="big">be</span><br><span class="amp">&amp;</span><span class="big">help</span> them<br>become what they<br>are capable of<br><span class="big">being</span></p>
    </div>
    <div class="quote q-bottom">
      <p class="predict-caps">THE</p>
      <p class="predict-caps bold">BEST WAY</p>
      <p class="predict-red"><small>TO </small>PREDICT</p>
      <p class="predict-caps">YOUR FUTURE</p>
      <p class="predict-caps">IS TO</p>
      <p class="predict-create">CREATE</p>
      <p class="predict-it">IT</p>
    </div>
  </section>

</main>
</body>
</html>
```